Website for Youth Orchestra to sell tickets and attract young musicians

We are looking for a new website design for a Youth Orchestra; one of the best classical youth orchestras in the county. This project is the design only. <br/><br/>The website serves two main purposes:<br/>• Selling tickets for concerts and performances of the orchestra<br/>• Recruiting young musicians to do audition for the orchestra<br/>
Updates

Target Market(s)

Classical music lovers with a special interest in young upcoming musicians.
Young talented musicians

Number of Pages Required

2 page

Colors
ec1f27

Requirements
Must have
• - A Picture on the front page that promotes the main upcomming event
• - Attention for recruiting new musicians
• - Pictures with young musicians (white back ground, see examples)
• - Responsive
• - Please use the logo attached
Should not have
• The brown colors of the current website (kvb-veldhorst.example)

```html
<!DOCTYPE html>
<html lang="nl">
<head>
<meta charset="utf-8">
<title>Veldhorst Jeugd Orkest</title>
<link rel="stylesheet" href="https://fonts.googleapis.com/css2?family=Montserrat:wght@300;400;500;600;700&family=Berkshire+Swash&display=swap">
<style>
:root{
  --red:#ec1f27;
  --dark:#333333;
  --ink:#222222;
  --text:#555555;
  --cream:#f5f2e6;
  --pink:#fce8ea;
  --black:#0b0b0b;
  --line:#e3e3e3;
}
*{box-sizing:border-box;margin:0;padding:0}
html,body{width:1200px;height:4367px;overflow:hidden}
body{font-family:"Montserrat",sans-serif;color:var(--text);background:#fff;position:relative}
.abs{position:absolute}
.btn{position:absolute;background:var(--red);color:#fff;border-radius:20px;font-size:13px;font-weight:500;display:flex;align-items:center;justify-content:center;gap:8px}
.btn-outline{background:#fff;color:var(--red);border:2px solid var(--red)}
.section-title{position:absolute;left:0;width:1200px;text-align:center;font-weight:300;font-size:36px;color:var(--ink)}
.divider{position:absolute;left:560px;width:80px;height:14px}
.divider::before{content:"";position:absolute;left:0;right:0;top:7px;height:1px;background:#ccc}
.divider::after{content:"";position:absolute;left:33px;top:0;width:14px;height:14px;border-radius:50%;background:var(--red);box-shadow:0 0 0 4px #fff}
.cream .divider::after{box-shadow:0 0 0 4px var(--cream)}
p{font-size:12px;line-height:23px}

/* header */
.topbar{top:0;left:0;width:1200px;height:46px;background:#fff}
.mail{left:142px;top:8px;display:flex;align-items:center;gap:10px;font-size:12px;color:var(--ink)}
.mail i{width:30px;height:30px;border-radius:50%;background:var(--red);display:flex;align-items:center;justify-content:center}
.navbar{top:46px;left:0;width:1200px;height:42px;background:var(--dark)}
.nav{position:absolute;top:0;height:42px;display:flex;align-items:center;gap:28px;font-size:11px;color:#fff;font-weight:500}
.nav .active{border-bottom:2px solid #fff;padding:12px 0 10px}
.brand{left:0;top:14px;width:1200px;display:flex;justify-content:center;align-items:center;gap:8px;font-size:15px;font-weight:600;color:var(--red)}
.brand i{width:12px;height:12px;border-radius:50%;background:var(--red)}

/* hero */
.hero{top:88px;left:0;width:1200px;height:485px;background:linear-gradient(90deg,#f4f5f6 0%,#eceef0 45%,#e6e6e6 100%)}
.hero-photo{left:560px;top:0;width:640px;height:485px;background:linear-gradient(180deg,#f1f1f1,#dedbd8 70%,#cfcac4)}
.hero h1{position:absolute;left:142px;top:95px;font-family:"Berkshire Swash",cursive;font-weight:400;color:#2a2a2a;font-size:52px;line-height:60px}
.hero h1 em{font-style:normal;color:var(--red);font-size:36px;display:block;line-height:44px}
.hero p{position:absolute;left:142px;top:268px;width:350px;font-size:12.5px;color:#444}

/* about */
.about-photo{left:142px;top:644px;width:430px;height:430px;border-radius:50%;background:radial-gradient(circle at 55% 45%,#f3efdc 0%,#ece6cd 60%,#d9cfae 100%)}
.about h2{position:absolute;left:629px;top:650px;font-size:36px;font-weight:300;color:var(--ink)}
.about .divider{left:629px;top:700px;width:30px}
.about .divider::before{display:none}
.about .divider::after{left:0}
.about h4{position:absolute;left:629px;top:738px;font-size:12px;color:var(--ink);font-weight:600}
.about p{position:absolute;left:629px;width:440px;font-size:11.5px;color:#666}

/* shows */
.shows{top:1144px;left:0;width:1200px;height:580px;background:var(--cream)}
.events{left:142px;top:164px;width:917px;height:272px;background:#fff;box-shadow:0 2px 10px rgba(0,0,0,.08)}
.ev-head{height:44px;display:flex;border-bottom:1px solid var(--line);font-size:11px;font-weight:500;color:var(--ink)}
.ev-head div{flex:1;display:flex;align-items:center;justify-content:center;gap:8px}
.ev-head div+div{border-left:1px solid var(--line);margin:12px 0}
.ev-row{position:relative;height:76px;display:flex;align-items:center;border-bottom:1px solid #f0f0f0}
.ev-row.raised{box-shadow:0 4px 14px rgba(0,0,0,.12);margin:0 -6px;padding:0 6px;z-index:2;background:#fff}
.ev-date{width:80px;text-align:center;font-size:10px;color:var(--ink);line-height:13px;border-right:1px solid var(--line)}
.ev-date b{font-size:11px;font-weight:700;display:block}
.ev-title{margin-left:25px;width:445px;font-size:11px;font-weight:600;color:var(--ink)}
.ev-title small{display:block;font-weight:400;font-size:10px;color:#777;margin-top:3px}
.ev-meta{display:flex;align-items:center;gap:8px;font-size:10px;color:#777;width:130px}
.ev-time{display:flex;align-items:center;gap:8px;font-size:10px;color:#777;width:120px}
.ticket-btn{position:absolute;right:20px;width:98px;height:30px;border-radius:15px;background:var(--red);color:#fff;font-size:10px;font-weight:700;display:flex;align-items:center;justify-content:center;letter-spacing:.5px}

/* musicians */
.card{top:1881px;width:212px;height:311px;background:#fff;box-shadow:0 2px 10px rgba(0,0,0,.1);text-align:center}
.card .ph{height:246px}
.card h5{font-size:14px;font-weight:600;color:var(--ink);margin-top:12px}
.card span{font-size:12px;color:#666}

/* mission */
.mv-box{left:142px;top:2368px;width:917px;height:305px;background:#fff;box-shadow:0 2px 14px rgba(0,0,0,.1)}
.mv-box .sep{position:absolute;left:458px;top:40px;width:0;height:240px;border-left:1px dashed #ddd}
.mv-name{left:142px;top:2380px;width:917px;text-align:center;font-size:14px;font-weight:600;color:var(--red)}
.mv-col{position:absolute;top:0;width:458px;text-align:center}
.mv-col h5{font-size:16px;font-weight:600;color:var(--ink);margin-top:112px}
.mv-col p{font-size:11px;line-height:23px;color:#666;padding:0 26px;margin-top:10px}

/* tickets */
.online p{position:absolute;left:0;width:1200px;text-align:center;font-size:12px}
.ticket{left:503px;top:2963px;width:192px;height:85px;background:linear-gradient(90deg,#2a2a2a 0 12px,#efe9cf 12px 180px,#2a2a2a 180px)}

/* career */
.career{top:3115px;left:0;width:1200px;height:482px;background:var(--pink)}
.career-photo{left:644px;top:40px;width:458px;height:442px;background:linear-gradient(180deg,#f6d7da,#e9b7bd 55%,#2b2224 56%,#1e1a1b)}
.career h2{position:absolute;left:142px;top:122px;font-size:36px;font-weight:300;color:var(--ink)}
.career .divider{left:142px;top:172px;width:30px}
.career .divider::before{display:none}
.career .divider::after{left:0;box-shadow:0 0 0 4px var(--pink)}
.career p{position:absolute;left:142px;top:208px;width:430px;font-size:11.5px;color:#555}

/* newsletter */
.news-title{left:200px;top:3710px;width:254px;text-align:right;font-size:34px;font-weight:300;color:var(--ink);line-height:46px}
.news-line{left:480px;top:3680px;width:1px;height:150px;background:#ddd}
.news-lead{left:515px;top:3720px;font-size:12px;font-weight:600;color:var(--ink)}
.news-form{left:515px;top:3749px;width:453px;height:38px;display:flex}
.news-form .input{flex:1;border:1px solid #ccc;border-right:0;border-radius:19px 0 0 19px;font-size:10px;color:#999;display:flex;align-items:center;padding-left:16px}
.news-form .go{width:110px;background:var(--red);color:#fff;border-radius:0 19px 19px 0;font-size:13px;font-weight:500;display:flex;align-items:center;justify-content:center}

/* footer */
.footer{top:3899px;left:0;width:1200px;height:432px;background:var(--black);color:#fff}
.fcol{position:absolute;top:68px}
.fcol h6{font-size:16px;font-weight:500;margin-bottom:22px}
.fcol ul{list-style:none;font-size:12px;line-height:27px;color:#ddd}
.fdiv{position:absolute;top:68px;height:270px;border-left:1px dashed #444}
.contact-line{display:flex;gap:14px;font-size:12px;line-height:21px;color:#ddd;margin-bottom:16px}
.partner{display:inline-block;width:96px;height:66px;background:#fff;margin-right:10px}
.bottombar{top:4331px;left:0;width:1200px;height:36px;background:var(--red);color:#fff;font-size:11px}
.social{position:absolute;top:8px;width:22px;height:22px;border-radius:50%;background:#fff}
</style>
</head>
<body>

<!-- header -->
<div class="abs topbar"></div>
<div class="abs mail"><i><svg width="14" height="10" viewBox="0 0 14 10"><rect x="0.5" y="0.5" width="13" height="9" fill="none" stroke="#fff"/><path d="M1 1l6 5 6-5" fill="none" stroke="#fff"/></svg></i>info@veldhorstorkest.example</div>
<div class="abs brand"><i></i>Veldhorst Jeugd Orkest</div>
<div class="btn btn-outline" style="left:825px;top:8px;width:140px;height:30px;font-size:12px">Koop Kaartjes</div>
<div class="btn" style="left:974px;top:8px;width:84px;height:30px;font-size:12px">Log In</div>
<div class="abs navbar">
  <nav class="nav" style="left:148px"><span class="active">Home</span><span>Orkest</span><span>Speel Mee</span><span>Concerten</span><span>Tournees</span></nav>
  <nav class="nav" style="left:716px"><span>Partners</span><span>Vrienden</span><span>Oudlesden</span><span>Contact &amp; Organisatie</span></nav>
</div>

<!-- hero -->
<section class="abs hero">
  <div class="abs hero-photo" role="img" aria-label="Vier jonge violistes en een celliste in witte jurken in een witte studio"></div>
  <h1><em>Welkom Bij</em>Veldhorst<br>Tickets Music</h1>
  <p>An orchestra with young  people that are very talented. Most of them are destined or are already a student at the conservatory of music.</p>
  <div class="btn" style="left:142px;top:356px;width:152px;height:35px">Koop Kaartjes</div>
</section>

<!-- about -->
<section class="about">
  <div class="abs about-photo" role="img" aria-label="Jonge violist in pak speelt viool"></div>
  <h2>Over VJO</h2>
  <div class="divider"></div>
  <h4>Het Veldhorst Jeugd Orkest speelt vol vuur!</h4>
  <p style="top:766px">Het Veldhorst Jeugd Orkest (VJO) is een jeugdorkest dat speelt in volledig symfonische bezetting. Het orkest telt circa zeventig jonge musici uit Veldhorst en omstreken, in de leeftijd van dertien tot vierentwintig jaar. De musici zijn merendeels middelbare scholieren en studenten. Het orkest repeteert iedere vrijdagavond in de St. Bonifatiuskerk te Veldhorst. Deze repetitie is openbaar toegankelijk. Wie wil komen luisteren, is welkom!</p>
  <p style="top:934px">Het VJO is opgericht in 1962 door twaalf kinderen van de Veldhorstse muziekschool en stond vijfentwintig jaar lang onder leiding van Joris van Dalen. Van 1987 tot aan 2005 was Pieter Aalders.</p>
  <div class="btn" style="left:629px;top:1022px;width:118px;height:34px">Lees Verder</div>
</section>

<!-- upcoming shows -->
<section class="abs shows cream">
  <h2 class="section-title" style="top:64px">Upcoming Shows</h2>
  <div class="divider" style="top:118px"></div>
  <div class="abs events">
    <div class="ev-head">
      <div><svg width="10" height="13" viewBox="0 0 10 13"><path d="M5 0a5 5 0 0 0-5 5c0 4 5 8 5 8s5-4 5-8a5 5 0 0 0-5-5z" fill="#ec1f27"/><circle cx="5" cy="5" r="2" fill="#fff"/></svg>Events Near All Location</div>
      <div><svg width="12" height="10" viewBox="0 0 12 10"><path d="M0 1h12M0 5h12M0 9h12" stroke="#ec1f27" stroke-width="1.6"/></svg>Filters</div>
    </div>
    <div class="ev-row">
      <div class="ev-date">Fri<b>JAN 31</b>7:00 pm</div>
      <div class="ev-title">Lorem ipsum dolor sit amet<small>Consectetuer adipiscing elit</small></div>
      <div class="ev-meta"><svg width="8" height="11" viewBox="0 0 10 13"><path d="M5 0a5 5 0 0 0-5 5c0 4 5 8 5 8s5-4 5-8a5 5 0 0 0-5-5z" fill="#ec1f27"/></svg>Lorem ipsum dolor</div>
      <div class="ev-time"><svg width="12" height="12" viewBox="0 0 12 12"><circle cx="6" cy="6" r="5" fill="none" stroke="#ec1f27"/><path d="M6 3v3h2" fill="none" stroke="#ec1f27"/></svg>8:00 pm</div>
      <div class="ticket-btn">TICKETS</div>
    </div>
    <div class="ev-row raised">
      <div class="ev-date">Sat<b>FEB 1</b>10:00 am</div>
      <div class="ev-title">Lorem ipsum dolor sit amet<small>Consectetuer adipiscing elit</small></div>
      <div class="ev-meta"><svg width="8" height="11" viewBox="0 0 10 13"><path d="M5 0a5 5 0 0 0-5 5c0 4 5 8 5 8s5-4 5-8a5 5 0 0 0-5-5z" fill="#ec1f27"/></svg>Lorem ipsum dolor</div>
      <div class="ev-time"><svg width="12" height="12" viewBox="0 0 12 12"><circle cx="6" cy="6" r="5" fill="none" stroke="#ec1f27"/><path d="M6 3v3h2" fill="none" stroke="#ec1f27"/></svg>8:00 pm</div>
      <div class="ticket-btn" style="right:26px">TICKETS</div>
    </div>
    <div class="ev-row">
      <div class="ev-date">Wed<b>FEB 4</b>12:00 am</div>
      <div class="ev-title">Lorem ipsum dolor sit amet<small>Consectetuer adipiscing elit</small></div>
      <div class="ev-meta"><svg width="8" height="11" viewBox="0 0 10 13"><path d="M5 0a5 5 0 0 0-5 5c0 4 5 8 5 8s5-4 5-8a5 5 0 0 0-5-5z" fill="#ec1f27"/></svg>Lorem ipsum dolor</div>
      <div class="ev-time"><svg width="12" height="12" viewBox="0 0 12 12"><circle cx="6" cy="6" r="5" fill="none" stroke="#ec1f27"/><path d="M6 3v3h2" fill="none" stroke="#ec1f27"/></svg>8:00 pm</div>
      <div class="ticket-btn">TICKETS</div>
    </div>
  </div>
  <div class="btn btn-outline" style="left:541px;top:472px;width:118px;height:34px">View All</div>
</section>

<!-- musicians -->
<h2 class="section-title" style="top:1784px">Musicians</h2>
<div class="divider" style="top:1838px"></div>
<div class="abs card" style="left:171px"><div class="ph" role="img" aria-label="Cellist in pak met cello" style="background:linear-gradient(135deg,#f2f2f2,#d7d9dc)"></div><h5>Elian Brouwer</h5><span>Klarinet</span></div>
<div class="abs card" style="left:407px"><div class="ph" role="img" aria-label="Jonge muzikant met tuba op straat" style="background:linear-gradient(135deg,#c9bda9,#8c7e6a)"></div><h5>Jasper Dekker</h5><span>Altviool</span></div>
<div class="abs card" style="left:642px"><div class="ph" role="img" aria-label="Violiste speelt viool" style="background:linear-gradient(135deg,#b88a3e,#5a3a1a)"></div><h5>Marit Visser</h5><span>Hobo</span></div>
<div class="abs card" style="left:878px"><div class="ph" role="img" aria-label="Violist in pak" style="background:linear-gradient(135deg,#e7dcc2,#c6b28a)"></div><h5>Joost Hendriks</h5><span>Slagwerk</span></div>

<!-- mission -->
<h2 class="section-title" style="top:2261px">Missie, Visie &amp; Solisten</h2>
<div class="divider" style="top:2316px"></div>
<div class="abs mv-box">
  <div class="sep"></div>
  <div class="mv-col" style="left:0">
    <svg class="abs" style="left:200px;top:38px" width="58" height="58" viewBox="0 0 58 58"><circle cx="27" cy="31" r="25" fill="none" stroke="#ec1f27" stroke-width="3"/><circle cx="27" cy="31" r="16" fill="none" stroke="#ec1f27" stroke-width="3"/><circle cx="27" cy="31" r="6" fill="#ec1f27"/><path d="M27 31L52 6M44 6h8v8" fill="none" stroke="#ec1f27" stroke-width="3"/></svg>
    <h5>Missie</h5>
    <p>Het Veldhorst Jeugd Orkest (VJO) wil voor de jeugd uit Veldhorst en omstreken een uitdagend podium zijn, waarop zij haar muzikale talent volledig tot bloei kan laten komen.</p>
  </div>
  <div class="mv-col" style="left:458px">
    <svg class="abs" style="left:198px;top:50px" width="62" height="34" viewBox="0 0 62 34"><path d="M2 17C14 3 48 3 60 17C48 31 14 31 2 17z" fill="none" stroke="#222" stroke-width="2.5"/><circle cx="31" cy="17" r="9" fill="none" stroke="#222" stroke-width="2.5"/><circle cx="31" cy="17" r="3.5" fill="#ec1f27"/></svg>
    <h5>Visie</h5>
    <p>Het VJO wil een zo breed mogelijk publiek bereiken door prikkelende symfonische programma's samen te stellen. We nodigen daarbij graag andere kunstdisciplines uit zoals bijvoorbeeld bij onze educatievoorstellingen. Denk daarbij ook aan het ten gehore brengen van (nieuwe) composities uit andere muziekgenres zoals pop, jazz, tango &amp; klezmer. Voorbeelden daarvan ziet u bij partners in music.</p>
  </div>
</div>
<div class="abs mv-name">Veldhorst Jeugd Orkest</div>
<div class="btn" style="left:541px;top:2707px;width:118px;height:34px">Lees Verder</div>

<!-- online tickets -->
<section class="online">
  <h2 class="section-title" style="top:2803px">Online Kaarten Bestellen</h2>
  <div class="divider" style="top:2858px"></div>
  <p style="top:2893px">Het orkest geeft meerdere concerten per jaar en verkoopt online tickets om hun activiteiten te financieren.</p>
  <p style="top:2920px;font-weight:600;color:#222">Ga direct naar onze bestelpagina</p>
  <div class="abs ticket" role="img" aria-label="Concertticket 12 januari 2020, 14:30 uur"></div>
</section>

<!-- career -->
<section class="abs career">
  <div class="abs career-photo" role="img" aria-label="Jonge violiste in zwart speelt viool"></div>
  <h2>Musical Career</h2>
  <div class="divider"></div>
  <p>Een orkest met jonge mensen die zeer getalenteerd zijn. De meeste zijn voorbestemd of studeren al aan het conservatorium van muziek. Het orkest trekt jonge muzikanten uit andere orkesten aan die een volgende stap in hun muzikale carrière willen maken.</p>
  <div class="btn" style="left:142px;top:334px;width:98px;height:34px">join now</div>
</section>

<!-- newsletter -->
<div class="abs news-title">Nieuwsbrief<br>Inschrijven</div>
<div class="abs news-line"></div>
<div class="abs news-lead">Abonneer u op onze nieuwsbrief voor de nieuwste update in uw inbox</div>
<div class="abs news-form"><div class="input">Vul je e-mailadres in</div><div class="go">Abonneren</div></div>

<!-- footer -->
<footer class="abs footer">
  <div class="fcol" style="left:142px"><h6>Snelle links</h6><ul><li>Huis</li><li>Orkest</li><li>Speel Mee</li><li>Concerten</li><li>Tournees</li><li>Partners</li><li>Vrienden</li><li>Oudlesden</li><li>Contact &amp; Organisatie</li></ul></div>
  <div class="fdiv" style="left:384px"></div>
  <div class="fcol" style="left:503px"><h6>Andere links</h6><ul><li>Commissies</li><li>Dirigent</li><li>gedragscode</li><li>Orkestleden</li><li>Auditiedata</li><li>Auditieformulier</li><li>Repetitie Bezoeken</li><li>Vacatures</li><li>Bestuur</li><li>Word Vriend</li></ul></div>
  <div class="fdiv" style="left:730px"></div>
  <div class="fcol" style="left:849px">
    <h6>Contact details</h6>
    <div class="contact-line"><svg width="12" height="16" viewBox="0 0 10 13"><path d="M5 0a5 5 0 0 0-5 5c0 4 5 8 5 8s5-4 5-8a5 5 0 0 0-5-5z" fill="#ec1f27"/><circle cx="5" cy="5" r="2" fill="#0b0b0b"/></svg><div><b style="color:#fff;font-weight:600">Veldhorst Tickets Music</b><br>Veldhorst Youth Orchestra<br>Postbus 412, 7200AB Veldhorst</div></div>
    <div class="contact-line"><svg width="12" height="12" viewBox="0 0 12 12"><path d="M2 1l2.5 0 1 3-1.5 1a7 7 0 0 0 3 3l1-1.5 3 1V10c0 .8-1 1.5-2 1.3C5 10.5 1.5 7 .7 3 .5 2 1.2 1 2 1z" fill="#ec1f27"/></svg><span style="color:#555">0612 345 678</span></div>
    <div class="contact-line"><svg width="12" height="10" viewBox="0 0 14 10"><rect width="14" height="10" fill="#ec1f27"/><path d="M1 1l6 5 6-5" fill="none" stroke="#0b0b0b"/></svg>info@kvb-veldhorst.example</div>
    <h6 style="margin-top:6px;margin-bottom:14px">Onze Partners</h6>
    <span class="partner"></span><span class="partner"></span>
  </div>
</footer>
<div class="abs bottombar">
  <div class="abs" style="left:142px;top:11px">© 2020 Veldhorst Jeugd Orkest. All Rights Reserved.</div>
  <span class="social" style="left:973px"></span><span class="social" style="left:1004px"></span><span class="social" style="left:1035px"></span>
</div>

</body>
</html>
```